Design for Employee Baseball Cards

Looking to design baseball cards for my employees. Trying to replicate famous baseball card design with swapping in an employee and listing there stats and fun facts. These cards will be inserted into boxes so customers can receive with their orders. Cards allow customers to put a face to the name they've always corresponded with, which makes their experience personable and more memorable.

Looking for a front and back design template. We are open to the design, but would like it to resemble a baseball/playing card.
Size: 2.5" x 3.5" vertical
Here is our website which can be referenced for color pallet and tone.
https://www.crateswithmarlow.com/

Attached is an example of a vintage baseball. Can we see some versions like this?

Front
- Person's name
- Title/Department
- Crates With Marlow logo
- Person's photo - this will be an action shot like a baseball card

Back
I'm open to the design and content of the back. We want it to resemble a back of a baseball card as best as possible. Normally, baseball cards will have stats by year. Instead, we can have stats and fun facts like the following

Items for Back
- Bio
- Year started at CWM
- Department
- Years of experience
- Specialty
- Secret skill
- What you love about CWM
- Favorite quote
- Fun fact
- Passion outside of CWM
- Person's photo - we can include a smaller headshot

Font styles to use
Sans Serif

Colors
0054AA
0677BA
7BADD7
CADEEF
E8F1F8

Requirements
Must have
• The deliverable must be a template PSD or AI that we can swap in photos and edit text for each person's card.

```html
<!DOCTYPE html>
<html lang="en">
<head>
<meta charset="utf-8">
<title>Crates With Marlow – Employee Card</title>
<link rel="stylesheet" href="https://fonts.googleapis.com/css2?family=Oswald:wght@400;500;600;700&display=swap">
<style>
  :root {
    --navy: #1c3a6e;
    --blue: #2461b3;
    --tan: #c0b6a7;
    --white: #ffffff;
    --page: #ecebe8;
    --photo-light: #f5f5f6;
    --photo-dark: #c9ccd4;
  }
  * { margin: 0; padding: 0; box-sizing: border-box; }
  html, body { width: 1200px; height: 720px; overflow: hidden; }
  body {
    background: var(--page);
    font-family: "Oswald", "Arial Narrow", sans-serif;
    color: var(--navy);
    position: relative;
  }
  .card {
    position: absolute;
    top: 80px;
    width: 400px;
    height: 560px;
    background: var(--tan);
    overflow: hidden;
  }
  .card-front { left: 150px; }
  .card-back { left: 650px; }
  .card svg.frame { position: absolute; inset: 0; }
  .label { position: absolute; text-transform: uppercase; line-height: 1; white-space: nowrap; }

  /* Front */
  .brand {
    position: absolute; left: 34px; top: 44px;
    display: flex; align-items: center; gap: 8px;
  }
  .brand-square { width: 26px; height: 26px; background: var(--navy); }
  .brand-name { font-size: 17px; font-weight: 500; line-height: 1.05; width: 96px; }
  .title-caption { left: 214px; top: 22px; font-size: 16px; font-weight: 500; }
  .title-value { left: 202px; top: 44px; font-size: 30px; font-weight: 600; }
  .photo-main {
    position: absolute; left: 39px; top: 101px; width: 312px; height: 364px;
    border-radius: 9px;
    background: linear-gradient(180deg, var(--photo-light) 0%, var(--photo-light) 45%, var(--photo-dark) 100%);
  }
  .name-caption { left: 28px; top: 490px; font-size: 38px; font-weight: 600; }
  .name-value { left: 180px; top: 488px; font-size: 38px; font-weight: 600; }

  /* Back */
  .headshot {
    position: absolute; left: 44px; top: 16px; width: 136px; height: 136px;
    border-radius: 50%;
    background: radial-gradient(circle at 50% 45%, var(--photo-light) 0%, var(--photo-dark) 100%);
  }
  .dept-caption { left: 230px; top: 30px; font-size: 22px; font-weight: 600; color: var(--white); }
  .bio-caption { left: 188px; top: 110px; font-size: 19px; font-weight: 600; }
  .stat-caption { top: 178px; font-size: 13px; font-weight: 500; color: var(--white); }
  .stat-started { left: 60px; }
  .stat-experience { left: 244px; }
  .fact { left: 24px; font-size: 13px; font-weight: 600; }
  .fact-quote { top: 226px; }
  .fact-fun { top: 252px; }
  .fact-skill { top: 278px; }
  .fact-specialty { top: 304px; }
  .tab-caption {
    left: 128px; width: 144px; text-align: center;
    font-size: 12px; font-weight: 500; color: var(--white);
  }
  .tab-love { top: 343px; }
  .tab-passion { top: 446px; }
</style>
</head>
<body>

  <section class="card card-front">
    <svg class="frame" width="400" height="560" viewBox="0 0 400 560" aria-hidden="true">
      <path d="M16,66 Q16,40 42,38 L194,32 L178,64 L196,96 L360,90 Q380,90 380,112 L382,520 Q382,540 362,540 L150,544 L174,510 L148,480 L46,482 Q22,482 20,458 Z"
            fill="var(--white)" stroke="var(--navy)" stroke-width="4" stroke-linejoin="round"/>
      <rect x="36" y="98" width="318" height="370" rx="12" fill="var(--white)" stroke="var(--navy)" stroke-width="5"/>
    </svg>
    <div class="brand">
      <span class="brand-square"></span>
      <span class="brand-name">Crates With Marlow</span>
    </div>
    <div class="label title-caption">Title/Department</div>
    <div class="label title-value">Salesperson</div>
    <div class="photo-main" role="img" aria-label="Employee action photo"></div>
    <div class="label name-caption">Name</div>
    <div class="label name-value">Dan Keller</div>
  </section>

  <section class="card card-back">
    <svg class="frame" width="400" height="560" viewBox="0 0 400 560" aria-hidden="true">
      <rect x="12" y="14" width="376" height="528" rx="26" fill="var(--white)" stroke="var(--navy)" stroke-width="4"/>
      <path d="M150,16 L360,16 Q386,16 386,42 L386,128 Q384,102 358,102 L150,98 Z" fill="var(--blue)"/>
      <path d="M150,98 L358,102 Q384,104 386,128" fill="none" stroke="var(--navy)" stroke-width="4"/>
      <rect x="12" y="170" width="376" height="46" fill="var(--navy)"/>
      <line x1="200" y1="178" x2="200" y2="210" stroke="var(--white)" stroke-width="2"/>
      <line x1="12" y1="336" x2="388" y2="336" stroke="var(--navy)" stroke-width="2"/>
      <rect x="128" y="336" width="144" height="26" fill="var(--navy)"/>
      <line x1="12" y1="438" x2="388" y2="438" stroke="var(--navy)" stroke-width="2"/>
      <rect x="128" y="438" width="144" height="26" fill="var(--navy)"/>
      <circle cx="112" cy="84" r="70" fill="var(--white)" stroke="var(--navy)" stroke-width="5"/>
    </svg>
    <div class="headshot" role="img" aria-label="Employee headshot"></div>
    <div class="label dept-caption">Department</div>
    <div class="label bio-caption">Bio:</div>
    <div class="label stat-caption stat-started">Year started at CWM</div>
    <div class="label stat-caption stat-experience">Years of experience</div>
    <div class="label fact fact-quote">Favorite quote:</div>
    <div class="label fact fact-fun">Fun fact:</div>
    <div class="label fact fact-skill">Secret skill:</div>
    <div class="label fact fact-specialty">Specialty:</div>
    <div class="label tab-caption tab-love">What you love about CWM</div>
    <div class="label tab-caption tab-passion">Passion outside of CWM</div>
  </section>

</body>
</html>
```